Mira Tails

im a dog walker, pet sitter and dog groomer. I can look after all pets from once a day pop in feeds of cats to small holdings and exotics. have 10 years experience in the industry. I can look after peoples dogs for the day while they are out or for longer if on holiday. I walk dogs when people are at work so the dogs get to have fun too. I do house sitting so all your animals are looked after together. you have designed my business cards and I wanted the 'mira tails' with the paw to be the same on the leaflets. I have spoken to printolane and they have sent a pdf file of business card and said it can be cropped. please let me know if this cant be done
im also a qualified canine hydrotherapist

Target Market(s)

pet owners

Industry/Entity Type

Pet

Requirements
Must have
• my phone number 07834562719
• email miratails@mailbox-example.co.uk
• area; Tunbridge wells, Sevenoaks and surrounding areas
• I want it almost done as bullet points with the main things being the dog walking and the pet sitting.
Nice to have
• cartoon animals like business card not the cartoons with big eyes

```html
<!DOCTYPE html>
<html lang="en">
<head>
<meta charset="utf-8">
<title>Mira Tails – Leaflet</title>
<link href="https://fonts.googleapis.com/css2?family=Bree+Serif&family=Open+Sans:wght@400;700&family=Roboto+Condensed:wght@700&display=swap" rel="stylesheet">
<style>
  :root{
    --page:#e9e6e1;
    --paper:#f3f1ee;
    --grass-light:#8fd04a;
    --grass-dark:#3f8f1f;
    --purple:#7d5aa8;
    --purple-deep:#6a4795;
    --gold:#f2c14e;
    --red:#e0262b;
    --ink:#2c2c2c;
    --grey:#555555;
    --white:#ffffff;
  }
  *{box-sizing:border-box;margin:0;padding:0}
  html,body{width:973px;height:1200px;overflow:hidden;background:var(--page)}
  .leaflet{
    position:absolute;left:82px;top:30px;
    width:513px;height:723px;
    transform:scale(1.577);transform-origin:0 0;
    background:var(--paper);overflow:hidden;
    box-shadow:0 2px 6px rgba(0,0,0,.25);
  }
  .backdrop{position:absolute;inset:0;width:100%;height:100%}
  .photo{position:absolute}
  .photo--pets-top{left:285px;top:0;width:228px;height:262px;
    background:radial-gradient(ellipse at 50% 55%,#c9a877 0%,#a7926e 45%,rgba(120,150,80,0) 75%)}
  .photo--owner-dog{left:255px;top:232px;width:258px;height:405px;
    background:radial-gradient(ellipse at 55% 45%,#e9dcc5 0%,#d9a7a3 40%,#b06a5a 60%,rgba(243,241,238,0) 80%)}
  .illustration--farm{left:26px;top:446px;width:134px;height:158px;
    background:radial-gradient(ellipse at 50% 55%,#8a5a3a 0%,#b58a60 45%,rgba(243,241,238,0) 75%)}
  .photo--pup-kitten{left:172px;top:500px;width:165px;height:158px;
    background:radial-gradient(ellipse at 50% 55%,#5a5a5a 0%,#b4aaa0 45%,rgba(243,241,238,0) 75%)}
  .services{position:absolute;left:28px;top:44px;list-style:none;
    font-family:"Roboto Condensed",Arial,sans-serif;font-weight:700;font-size:26px;
    line-height:34.5px;color:var(--white);text-shadow:1px 2px 3px rgba(0,0,0,.45)}
  .brand{position:absolute;left:62px;top:290px;display:flex;align-items:center;gap:12px}
  .brand__dot{width:38px;height:38px;border-radius:50%;background:var(--gold)}
  .brand__name{font-family:"Bree Serif",Georgia,serif;font-size:32px;color:var(--purple)}
  .area{position:absolute;left:70px;top:383px;width:176px;border-top:1px solid #8a8a8a;
    padding-top:6px;text-align:center;font-family:"Open Sans",Arial,sans-serif;
    font-size:12.5px;line-height:17px;color:var(--grey)}
  .badge{position:absolute;left:343px;top:536px;width:120px;height:120px;border-radius:50%;
    background:var(--gold);display:flex;align-items:center;justify-content:center}
  .badge__inner{width:106px;height:106px;border-radius:50%;background:var(--red);
    border:2px solid #2a6fb7;display:flex;align-items:center;justify-content:center;
    text-align:center;font-family:"Bree Serif",Georgia,serif;font-size:16px;line-height:17px;color:var(--white)}
  .credential{position:absolute;left:313px;top:645px;width:186px;height:22px;border-radius:11px;
    background:var(--gold);font-family:"Open Sans",Arial,sans-serif;font-weight:700;
    font-size:10.5px;line-height:22px;text-align:center;color:var(--ink)}
  .contact-name{position:absolute;left:26px;top:648px;font-family:"Bree Serif",Georgia,serif;
    font-size:27px;color:var(--white)}
  .contact-email{position:absolute;left:26px;top:688px;font-family:"Open Sans",Arial,sans-serif;
    font-weight:700;font-size:14px;color:var(--white)}
  .contact-phone{position:absolute;left:312px;top:680px;font-family:"Open Sans",Arial,sans-serif;
    font-weight:700;font-size:22px;color:var(--white)}
</style>
</head>
<body>
<main class="leaflet">
  <svg class="backdrop" viewBox="0 0 513 723" aria-hidden="true">
    <defs>
      <linearGradient id="grass" x1="0" y1="0" x2="0" y2="1">
        <stop offset="0" stop-color="#3c6b2a"/>
        <stop offset=".12" stop-color="var(--grass-dark)"/>
        <stop offset=".5" stop-color="var(--grass-light)"/>
        <stop offset="1" stop-color="#5fae2e"/>
      </linearGradient>
    </defs>
    <path d="M0 0H513V262C400 225 240 198 0 218Z" fill="url(#grass)"/>
    <path d="M0 212C160 186 340 200 513 262V282C340 222 170 220 0 262Z" fill="var(--purple)"/>
    <path d="M0 262C170 222 340 224 513 284V292C340 236 170 236 0 276Z" fill="var(--gold)"/>
    <path d="M0 614C160 596 340 612 513 628V723H0Z" fill="var(--white)"/>
    <path d="M0 620C160 602 340 618 513 634V723H0Z" fill="var(--gold)"/>
    <path d="M0 628C160 612 340 628 513 645V723H0Z" fill="var(--purple)"/>
  </svg>

  <div class="photo photo--pets-top" role="img" aria-label="Photo of a puppy, kittens and small birds on the lawn"></div>
  <div class="photo photo--owner-dog" role="img" aria-label="Photo of a smiling woman hugging a labrador puppy"></div>
  <div class="photo illustration--farm" role="img" aria-label="Illustration of a dog, rabbit, cat, hen and frog"></div>
  <div class="photo photo--pup-kitten" role="img" aria-label="Photo of a french bulldog puppy and a tabby kitten"></div>

  <ul class="services">
    <li>Dog Walking</li>
    <li>Pet/House Sitting</li>
    <li>Dog Grooming</li>
    <li>Small Holder Knowledge</li>
  </ul>

  <div class="brand">
    <span class="brand__dot"></span>
    <span class="brand__name">Mira Tails</span>
  </div>
  <p class="area">Tunbridge Wells, Sevenoaks<br>and Surrounding Areas</p>

  <div class="badge"><div class="badge__inner">10 Years<br>Experience<br>in animal<br>industry</div></div>
  <p class="credential">Qualified Canine Hydrotherapist</p>

  <p class="contact-name">Mira Dale</p>
  <p class="contact-email">miratails@mailbox-example.co.uk</p>
  <p class="contact-phone">07834.562.719</p>
</main>
</body>
</html>
```